Financial Advisor Resource Firm needs business card design

Need business card design for company in Omaha NE called Tallowbrook Alliance. We provide resources to financial advisors....workshop programs, retirement analysis, and insurance planning. I would like to see designs that use grays, greens, black, and white colors. The final design should communicate 'collaboration' and be simple yet attractive to financial planning clients. I will attached our logo and another picture of a puzzle piece coming together. I would like the incorporate the puzzle picture somehow, maybe on the back somehow, with color or just the gray scale....OR, the picture be the front of the card with 'Tallowbrook' definition on it (see upload) and then company logo, employee name, title, address on the back (see ppt uploaded). The following disclosure needs to be included somewhere- Advisory services offered through Hemstead Ledger, LLC.
Updates

I uploaded a svg and ai file of the logo

Target Market(s)

Financial planning clients and financial advisors....so pretty diverse age range of about 40-70.

Industry/Entity Type

Financial Planning

Contact Information for Business Card

Morris P. Quillfen, MBA
Founder/President
5327 E. Larkspur Avenue
Suite 418
Omaha, NE 68907
Phone- (402) 555-0147
Cell- (402) 555-0193
Fax- (402) 555-0126
email- morris@tallowbrookplan.example
web address- www.tallowbrookplan.example

Colors
1b1b1b
474747
d3d3d3
ffffff
9bcb3c
abd036

Requirements
Must have
• Must include logo provided, must be 2 sided, and must have disclosure...all of these items listed in project description

```html
<!DOCTYPE html>
<html lang="en">
<head>
<meta charset="utf-8">
<title>Tallowbrook Alliance – Business Card</title>
<link rel="stylesheet" href="https://fonts.googleapis.com/css2?family=Roboto:wght@400;500;700&display=swap">
<style>
  :root {
    --ink: #1b1b1b;
    --charcoal: #474747;
    --silver: #d3d3d3;
    --white: #ffffff;
    --green: #9bcb3c;
    --lime: #abd036;
    --stage: #232323;
  }
  * { box-sizing: border-box; margin: 0; padding: 0; }
  html, body { width: 1200px; height: 1200px; overflow: hidden; }
  body {
    background: var(--stage);
    font-family: "Roboto", Arial, sans-serif;
    position: relative;
  }
  .card {
    position: absolute;
    top: 162px;
    width: 500px;
    height: 875px;
    overflow: hidden;
  }
  .card--front { left: 60px; background: var(--white); }
  .card--back { left: 640px; background: var(--silver); }

  /* shared wordmark */
  .wordmark {
    display: flex;
    align-items: center;
    gap: 14px;
    color: var(--ink);
    font-weight: 700;
    text-transform: uppercase;
    letter-spacing: 1px;
    line-height: 1.05;
  }
  .wordmark__dot {
    flex: none;
    border-radius: 50%;
    background: var(--green);
  }

  /* front */
  .front__logo {
    position: absolute;
    top: 70px; left: 0; right: 0;
    justify-content: center;
    font-size: 34px;
  }
  .front__logo .wordmark__dot { width: 26px; height: 26px; }
  .front__identity {
    position: absolute;
    top: 200px; left: 44px; right: 40px;
  }
  .name {
    font-size: 38px;
    font-weight: 500;
    color: var(--ink);
    white-space: nowrap;
  }
  .name__first { color: var(--green); font-weight: 700; font-size: 32px; letter-spacing: 1px; }
  .name__cred { font-size: 15px; font-weight: 500; margin-left: 6px; color: var(--ink); }
  .title { margin-top: 10px; font-size: 21px; color: var(--charcoal); }

  .front__photo {
    position: absolute;
    top: 300px; right: 0;
    width: 260px; height: 200px;
    background: linear-gradient(160deg, #f2f2f2 0%, #a9a9a9 45%, #6a6a6a 100%);
    clip-path: polygon(100% 0, 100% 100%, 0 100%);
  }
  .front__panel {
    position: absolute;
    top: 340px; left: 0; right: 0; bottom: 88px;
    background: linear-gradient(135deg, var(--charcoal) 0%, #2f2f2f 60%, var(--ink) 100%);
    clip-path: polygon(0 0, 48% 0, 100% 34%, 100% 100%, 0 100%);
    padding: 120px 40px 0 44px;
  }
  .contacts { list-style: none; }
  .contacts li {
    display: flex;
    align-items: flex-start;
    gap: 16px;
    color: var(--white);
    font-size: 18px;
    line-height: 1.35;
    margin-bottom: 14px;
  }
  .contacts svg { flex: none; width: 20px; height: 20px; margin-top: 1px; }
  .icon { fill: none; stroke: var(--green); stroke-width: 2; stroke-linecap: round; stroke-linejoin: round; }

  .disclosure {
    position: absolute;
    left: 0; right: 0; bottom: 0;
    height: 88px;
    background: var(--green);
    display: flex;
    align-items: center;
    justify-content: center;
    color: var(--ink);
    font-size: 17px;
    font-weight: 500;
  }

  /* back */
  .back__texture {
    position: absolute;
    inset: 0 0 355px 0;
    background: linear-gradient(135deg, #eeeeee 0%, var(--silver) 55%, #c4c4c4 100%);
  }
  .back__frame {
    position: absolute;
    inset: 28px;
    border: 1px solid var(--charcoal);
  }
  .back__logo {
    position: absolute;
    top: 220px; left: 0; right: 0;
    justify-content: center;
    font-size: 40px;
  }
  .back__logo .wordmark__dot { width: 30px; height: 30px; }
  .definition {
    position: absolute;
    top: 520px; left: 0; right: 0;
    height: 92px;
    background: var(--lime);
    display: flex;
    align-items: center;
    justify-content: center;
    text-align: center;
    color: var(--ink);
    font-size: 16px;
    line-height: 1.4;
    text-transform: uppercase;
    padding: 0 40px;
  }
  .back__photo {
    position: absolute;
    top: 612px; left: 0; right: 0; bottom: 0;
    background: radial-gradient(ellipse at 60% 45%, #d9d9d9 0%, #8c8c8c 45%, #3d3d3d 100%);
  }
</style>
</head>
<body>

<section class="card card--front" aria-label="Business card, contact side">
  <div class="wordmark front__logo">
    <span class="wordmark__dot"></span>
    <span>Tallowbrook<br>Alliance</span>
  </div>

  <div class="front__identity">
    <p class="name"><span class="name__first">MORRIS</span> P. Quillfen<span class="name__cred">MBA</span></p>
    <p class="title">Founder/President</p>
  </div>

  <div class="front__photo" role="img" aria-label="Grayscale photo of hands joining puzzle pieces"></div>

  <div class="front__panel">
    <ul class="contacts">
      <li>
        <svg viewBox="0 0 20 20"><path class="icon" d="M10 18s6-6 6-10a6 6 0 0 0-12 0c0 4 6 10 6 10z"/><circle class="icon" cx="10" cy="8" r="2"/></svg>
        <span>5327 E. Larkspur Avenue, Suite 418,<br>Omaha, NE 68907</span>
      </li>
      <li>
        <svg viewBox="0 0 20 20"><path class="icon" d="M4 4h12v10H4zM8 17h4"/></svg>
        <span>(402) 555-0147</span>
      </li>
      <li>
        <svg viewBox="0 0 20 20"><path class="icon" d="M5 2h3l1 4-2 1a10 10 0 0 0 6 6l1-2 4 1v3a2 2 0 0 1-2 2A15 15 0 0 1 3 4a2 2 0 0 1 2-2z"/></svg>
        <span>(402) 555-0193</span>
      </li>
      <li>
        <svg viewBox="0 0 20 20"><path class="icon" d="M6 8V2h8v6M3 8h14v9H3zM6 12h8"/></svg>
        <span>(402) 555-0126</span>
      </li>
      <li>
        <svg viewBox="0 0 20 20"><path class="icon" d="M2 4h16v12H2zM2 4l8 7 8-7"/></svg>
        <span>morris@tallowbrookplan.example</span>
      </li>
      <li>
        <svg viewBox="0 0 20 20"><circle class="icon" cx="10" cy="10" r="8"/><path class="icon" d="M2 10h16M10 2c3 3 3 13 0 16M10 2c-3 3-3 13 0 16"/></svg>
        <span>www.tallowbrookplan.example</span>
      </li>
    </ul>
  </div>

  <p class="disclosure">Advisory services offered through Hemstead Ledger, LLC.</p>
</section>

<section class="card card--back" aria-label="Business card, brand side">
  <div class="back__texture" role="img" aria-label="Light gray woven diagonal line pattern"></div>
  <div class="back__frame"></div>
  <div class="wordmark back__logo">
    <span class="wordmark__dot"></span>
    <span>Tallowbrook<br>Alliance</span>
  </div>
  <p class="definition">Tallowbrook : to come together and unite in<br>a common interest and focus</p>
  <div class="back__photo" role="img" aria-label="Grayscale photo of several hands fitting puzzle pieces together"></div>
</section>

</body>
</html>
```